Halvorn spray foam and Environmental

I have business cards but need new ones. The ones I have are very bland. Here is. Y company website http://www.halvornsprayfoam.ca

Also I can send you copies of the current cards
I would also need my current logo on the new design as well.. Also spray foam and Environmental

Industry/Entity Type

Business

Logo Text

Halvorn.

```html
<!DOCTYPE html>
<html lang="en">
<head>
<meta charset="utf-8">
<title>Halvorn Business Cards</title>
<link href="https://fonts.googleapis.com/css2?family=Lato:wght@700;900&display=swap" rel="stylesheet">
<style>
  :root {
    --stage: #2e4a60;
    --paper: #ffffff;
    --purple: #6f3a7f;
    --grey: #6f6a6a;
    --grey-text: #5f5a5a;
  }
  * { margin: 0; padding: 0; box-sizing: border-box; }
  html, body { width: 1200px; height: 1200px; overflow: hidden; background: var(--stage); }
  body { position: relative; font-family: "Lato", Arial, sans-serif; }

  .card { position: absolute; left: 181px; width: 838px; height: 480px; background: var(--paper); }
  .card--foam { top: 62px; }
  .card--enviro { top: 578px; }

  .info-panel { position: absolute; left: 457px; top: 0; width: 356px; height: 480px; overflow: hidden; }
  .card--foam .info-panel { background: var(--purple); }
  .card--enviro .info-panel { background: var(--grey); }
  .panel-notch { position: absolute; left: 0; top: 110px; width: 22px; height: 44px; }

  .brand-mark { position: absolute; left: 183px; top: 148px; width: 90px; height: 76px; border-radius: 5px; background: var(--purple); }
  .brand-name { position: absolute; left: 0; width: 457px; top: 238px; text-align: center; font-weight: 900; font-size: 64px; line-height: 1; letter-spacing: 3px; color: var(--purple); }
  .brand-division { position: absolute; left: 0; width: 457px; top: 305px; text-align: center; font-weight: 900; font-size: 31px; line-height: 1; }
  .card--foam .brand-division { letter-spacing: 2px; color: var(--purple); }
  .card--enviro .brand-division { letter-spacing: 2.5px; color: var(--grey-text); }

  .panel-title { position: absolute; left: 33px; top: 116px; font-weight: 900; font-size: 38px; line-height: 1; letter-spacing: 2px; color: var(--paper); white-space: nowrap; }
  .panel-title--long { top: 120px; font-size: 33px; letter-spacing: 1.5px; }
  .contact-list { position: absolute; left: 33px; top: 164px; list-style: none; color: var(--paper); }
  .contact-list li { display: flex; align-items: center; height: 27px; font-weight: 900; font-size: 20px; letter-spacing: 1.2px; white-space: nowrap; }
  .contact-list svg { width: 18px; height: 18px; margin-right: 12px; flex: none; }

  .services-title { position: absolute; left: 33px; top: 282px; width: 208px; padding-bottom: 4px; border-bottom: 1.5px solid var(--paper); font-weight: 900; font-size: 30px; line-height: 1; letter-spacing: 1.5px; color: var(--paper); }
  .services-list { position: absolute; left: 33px; top: 323px; font-weight: 900; font-size: 15px; line-height: 19px; letter-spacing: 1px; color: var(--paper); }
</style>
</head>
<body>

<section class="card card--foam">
  <span class="brand-mark"></span>
  <div class="brand-name">HALVORN</div>
  <div class="brand-division">SPRAY FOAM</div>
  <div class="info-panel">
    <svg class="panel-notch" viewBox="0 0 22 44"><polygon points="0,0 22,22 0,44" fill="#ffffff"/></svg>
    <h2 class="panel-title">SPRAY FOAM</h2>
    <ul class="contact-list">
      <li><svg viewBox="0 0 20 20"><circle cx="10" cy="10" r="10" fill="#fff"/><path d="M6.5 5.5l2 0 1 2.5-1.3 1a6 6 0 0 0 2.8 2.8l1-1.3 2.5 1v2a1 1 0 0 1-1 1A8.5 8.5 0 0 1 5.5 6.5a1 1 0 0 1 1-1z" fill="#6f3a7f"/></svg>604-555-0148</li>
      <li><svg viewBox="0 0 20 20"><circle cx="10" cy="10" r="10" fill="#fff"/><rect x="5" y="6.5" width="10" height="7" fill="none" stroke="#6f3a7f" stroke-width="1.3"/><path d="M5 6.5l5 4 5-4" fill="none" stroke="#6f3a7f" stroke-width="1.3"/></svg>halvornfoam@hvmail.ca</li>
      <li><svg viewBox="0 0 20 20"><circle cx="10" cy="10" r="10" fill="#fff"/><g fill="none" stroke="#6f3a7f" stroke-width="1.1"><circle cx="10" cy="10" r="5.5"/><ellipse cx="10" cy="10" rx="2.4" ry="5.5"/><path d="M4.5 10h11M5.3 7.3h9.4M5.3 12.7h9.4"/></g></svg>halvornsprayfoam.ca</li>
    </ul>
    <h3 class="services-title">SERVICES</h3>
    <p class="services-list">ROOFING FOAM, SLABJACKING,<br>2POUND / BATT INSULATION,<br>SOUND PROOFING, ATTIC BLOW IN.</p>
  </div>
</section>

<section class="card card--enviro">
  <span class="brand-mark"></span>
  <div class="brand-name">HALVORN</div>
  <div class="brand-division">ENVIRONMENTAL</div>
  <div class="info-panel">
    <svg class="panel-notch" viewBox="0 0 22 44"><polygon points="0,0 22,22 0,44" fill="#ffffff"/></svg>
    <h2 class="panel-title panel-title--long">ENVIRONMENTAL</h2>
    <ul class="contact-list">
      <li><svg viewBox="0 0 20 20"><circle cx="10" cy="10" r="10" fill="#fff"/><path d="M6.5 5.5l2 0 1 2.5-1.3 1a6 6 0 0 0 2.8 2.8l1-1.3 2.5 1v2a1 1 0 0 1-1 1A8.5 8.5 0 0 1 5.5 6.5a1 1 0 0 1 1-1z" fill="#6f6a6a"/></svg>604-555-0172</li>
      <li><svg viewBox="0 0 20 20"><circle cx="10" cy="10" r="10" fill="#fff"/><rect x="5" y="6.5" width="10" height="7" fill="none" stroke="#6f6a6a" stroke-width="1.3"/><path d="M5 6.5l5 4 5-4" fill="none" stroke="#6f6a6a" stroke-width="1.3"/></svg>enviro1@hvmail.ca</li>
      <li><svg viewBox="0 0 20 20"><circle cx="10" cy="10" r="10" fill="#fff"/><g fill="none" stroke="#6f6a6a" stroke-width="1.1"><circle cx="10" cy="10" r="5.5"/><ellipse cx="10" cy="10" rx="2.4" ry="5.5"/><path d="M4.5 10h11M5.3 7.3h9.4M5.3 12.7h9.4"/></g></svg>halvornenvironmental.ca</li>
    </ul>
    <h3 class="services-title">SERVICES</h3>
    <p class="services-list">AIR MONITORING, ASBESTOS<br>TESTING, ASBESTOS REMOVAL,<br>MOULD REMOVAL, BUILDING<br>DEMOLITION, LEAD TESTING</p>
  </div>
</section>

</body>
</html>
```